Law Firm from Estonia. E-S-T-O-N-I-A. Country of nice people and bad skiing weather

Just in case there is still a misunderstanding here - this is a project for the Letterhead, Logo and Business Card (i.e THREE designs). Due to some odd reason the system does not always show Logo and Business Card part - we have written an e-mail to the ArtHive support on that.

Our current business name is Varendi & Lust by two owners.

We want turquoise blue as our corporate colour – against black and white background. As per logo and letterhead design – we would like it to be simple, modern and elegant.

We would like our corporate identity to express the following: best, vanguard, trustworthiness. Our logo must be:
-Classy and precious
-Simple, clean and elegant
-Timeless
-Trustworthy and strong

You should be heading for something LETTERED (we're legal), SIMPLE (we make other people's problems simple), STRAIGHTFORWARD, CORPORATE and CONFIDENT.

1. The Logo shall consist of two main parts: The company name and the symbol.
-The Brand Name is: Varendi & Lust
-The Symbol must be easy to recognize and clear.
Please suggest 3 symbols.
The name and the symbol must be usable together and separately, in colour (blue-green) and black&white.

Once The Logo has been set, please develop a stationary with the following items:
-Business Card
-Letterhead A4

Suggest 3 of each.

We are looking forward to your designs.
Updates

Dear all, As per light blue colour - could you please use BlueGreen palette (i.e turquoise, aquamarine, cyan blue, sea green etc) - i.e blue should contain a little bit of green. The colour palette provided here does not contain the right tone - the green blue is too green. Our blue should be bluer, but still contain a hint of green. Like, for example, Silkenbay products. Thank you!

Dear all, I do not know if you can see your colleagues' designs participating in the same contest, but they look alike as if you are using the same template. Therefore may we suggest that you do not use this horizontal S-wave and do something more creative. Moreover, it's about the LETTER of the law and about being straight - there is nothing in Law that is about waves. Please do NOT use waves! Our logo should be STRAIGHT and SOLID, but ELEGANT. Like Orvée. If you use our initials for logo, you may use different fonts. Just V&L is not appealing, we could create it ourselves in TextPad. Perhaps putting a full stop at the end of the initials might be interesting. Or, for example, have a look at Dawnfield Computing logo, forming an interesting square from the letters. As per colours - the palette here in ArtHive is very limited and all the colours look dirty. We would like our colours to be bright and clean. May we also suggest that you use colour gradient in some of your designs. We do not insist, but it might make the simple design (that we want) a bit more interesting. Kind regards Maret

Dear all, One of our partners has just suggested the following: The Law Firm's line is like the surgical incision: quick, clean and sharp. We hope it inspires you. Regards Maret

Hello everybody Nobody has ever done it yet, but as a combination of M and K you could use two triangles - if you connect M's legs and turn it clockwise to make it look like K I have unloaded some pictures that just came to my mind. Could you suggest something like this (too) please? Thank you

Dear all, Since your perception of turquoise might be different from ours, please find below a link with the exact colour we want. http://www.tintsample.example/colors/34DDDD OUR LOGO SHOULD BE MONOCHROME - the only colours that are allowed are turquoise (you may use hues), black and white. Please do NOT suggest green & blue, blue & red, red & orange etc. Regards Maret

Reason: One day to the deadline and we are not happy with the results yet. We hope this little extension helps. Regards Maret

Target Market(s)

Our clients are:
- mid- to large-sized companies
- managed by our agemates (let us say 35 and over),
- who are well educated middle-class males, married with children
- western languages speaking (English, Estonian, Scandinavian)

Industry/Entity Type

Business

Font styles to use
Sans Serif
Script

Colors
ecf7f6
ecf7f5
86cfc6
34b8a4
00a98f
33a6d7

Requirements
Should not have
• The design should not use old-style fonts
The design should not use serif fonts
Please do not use inaccurate informal fonts either
Please do not include common stamps of Themis (balance, sword, hammer etc)
Please do not use waves

```html
<!DOCTYPE html>
<html lang="en">
<head>
<meta charset="utf-8">
<title>Varendi &amp; Lust — Letterhead</title>
<link href="https://fonts.googleapis.com/css2?family=Ubuntu:wght@300;400&display=swap" rel="stylesheet">
<style>
  :root {
    --backdrop: #c9dcdd;
    --paper: #ffffff;
    --ink: #3a3a3a;
    --ink-soft: #6a6a6a;
    --turquoise: #5cc5c9;
    --signature-tone: #e4ecec;
  }
  * { box-sizing: border-box; margin: 0; padding: 0; }
  html, body {
    width: 1200px; height: 1000px; overflow: hidden;
    background: var(--backdrop);
    font-family: "Ubuntu", sans-serif;
  }
  .letterhead {
    position: absolute; left: 267px; top: 30px;
    width: 665px; height: 940px;
    background: var(--paper);
    padding: 62px 78px 0 78px;
    color: var(--ink);
  }
  .brand { display: flex; align-items: center; gap: 10px; }
  .brand-square { width: 22px; height: 22px; background: var(--turquoise); }
  .brand-name {
    font-weight: 400; font-size: 17px; letter-spacing: 0.04em;
    text-transform: uppercase; color: var(--ink);
  }
  .letter-body {
    margin-top: 72px; font-weight: 300; font-size: 10px; line-height: 1.6;
    color: var(--ink-soft); text-align: justify;
  }
  .salutation { margin-bottom: 16px; }
  .letter-body p.paragraph { margin-bottom: 28px; }
  .closing-row { display: flex; justify-content: space-between; align-items: flex-end; }
  .signature {
    width: 150px; height: 46px; background: var(--signature-tone);
    border-radius: 4px; margin-right: 20px;
  }
  .sign-off { margin-top: 22px; }
  .contact-footer {
    position: absolute; left: 78px; right: 60px; bottom: 42px;
    display: flex; justify-content: flex-end; gap: 8px;
    font-size: 7.5px; font-weight: 300; color: var(--ink-soft);
  }
  .contact-label { color: var(--turquoise); margin-right: 3px; }
  .contact-divider { color: var(--turquoise); }
</style>
</head>
<body>
  <main class="letterhead">
    <header class="brand">
      <span class="brand-square"></span>
      <span class="brand-name">Varendi &amp; Lust</span>
    </header>

    <section class="letter-body">
      <p class="salutation">Dear Client</p>
      <p class="paragraph">Lorem ipsum dolor sit amet, consectetur adipiscing elit. Nulla sodales nisi vitae lorem ipsum dolor sit amet, consectetur adipiscing elit. Suspendisse feugiat eros nisl, a facilisis risus eleifend sed. Aliquam mauris enim, fermentum eu lacinia sit amet, laoreet eu leo. Nullam eleifend nulla in libero tristique, ac vulputate odio tincidunt. Etiam non condimentum tortor. Integer suscipit neque nec odio porttitor cursus. Phasellus a sapien blandit, suscipit justo id, condimentum ante. Morbi tristique justo risus, id mattis dui molestie ut. Nullam volutpat ut quam commodo faucibus. Pellentesque urna est, interdum in elit quis, pharetra elementum orci. Nam pharetra velit molestie justo placerat scelerisque.</p>
      <p class="paragraph">Nullam aliquam ligula ac sem aliquet varius. Nullam sed laoreet sapien. Fusce ultricies lobortis odio, sed imperdiet magna lacinia egestas. Morbi vitae varius nibh. Phasellus purus felis, congue id tempor quis, porttitor ut sem. Integer turpis nunc, posuere at quam interdum, interdum pharetra lectus. Fusce commodo sapien vel consequat tincidunt. Proin sed nisl dignissim, accumsan dui ut, luctus turpis. Praesent vulputate elementum nisl. Ut volutpat felis ut mi tincidunt, vitae accumsan quam porta. Sed malesuada bibendum lectus tempor ullamcorper. Nullam interdum diam velit, id porta elit congue quis.</p>
      <div class="closing-row">
        <p class="paragraph" style="max-width: 320px;">Pellentesque habitant morbi tristique senectus et netus et malesuada fames ac turpis egestas. Donec quis fermentum massa. Vivamus auctor tincidunt tellus, vel iaculis elit sagittis sit amet. Morbi aliquam pharetra lobortis. Mauris non iaculis ipsum. Morbi tortor ipsum, suscipit a laoreet sed, tempus non risus. Maecenas rhoncus vehicula est, sagittis vulputate magna ullamcorper non. Sed dignissim sapien sed rhoncus imperdiet.</p>
        <div class="signature" role="img" aria-label="Handwritten signature of the sender"></div>
      </div>
      <p class="sign-off">Best regards,</p>
    </section>

    <footer class="contact-footer">
      <span><span class="contact-label">Office</span>Kalda 12, Tallinn 10111</span>
      <span class="contact-divider">|</span>
      <span><span class="contact-label">Tel</span>+372 600 1200</span>
      <span class="contact-divider">|</span>
      <span><span class="contact-label">Fax</span>+372 600 1201</span>
      <span class="contact-divider">|</span>
      <span><span class="contact-label">Email</span>info@varendilust.ee</span>
      <span class="contact-divider">|</span>
      <span><span class="contact-label">Web</span>www.varendilust.ee</span>
    </footer>
  </main>
</body>
</html>
```